Banner ad design for Vantor Reach Ads

We are looking for a designer to develop a concept for banner ads for a Vantor Reach campaign we are building.

We have 3 business lines, shredding services, records management services and scanning services.

We are looking for 4 sets of ads to be created, one for each business line + one set that showcases all of our lines together.

For the design concepts, we would like to see a few sizes (banner, square, leaderboard, skyscraper, etc) for each.

The person chosen will then need to create the ads into all Vantor supported sizes -- 20 sizes total for each set of ads as per the Vantor size guidelines found on this page - https://help.vantor.example/vantor-ads/answer/4859210?hl=en&ref_topic=6082714#

A few items to note:
- Design should complement our existing brand/website look and feel (www.gold-kettle.ca)
- Each final ad must be 150Kb or less in size
- Final designs should be editable, meaning if we would like to change some copy in the design, we can do so using a well-known software (Canva, Photoshop/InDesign, etc)
- Some images are attached for use, but if you feel a different stock image is more suitable to to your design, please go ahead and use it.

Provided below is some messaging that can be used for each set of ads. Do not feel you need to use all of the messaging, it is provided for guidance.

SHREDDING SERVICES:

Possible Short Headline:
-- One-Time Shredding Services
-- Secure Shredding Services
-- Affordable On-Site Shredding

Possible Long Headline
-- Your Paper Can be Destroyed as Soon as the Next Business Day

Possible Descriptions:
-- QVRB AAA Certified On site shredding company. Service as soon as Next Day.
-- Secure and Affordable Toronto & GTA On-Site Shredding.
-- Certified, Affordable Office Shredding Since 2003.
-- Quick, no contact and affordable paper shredding services in Toronto & Southern Ontario.
-- Certified, Affordable Office Shredding Since 2003. Fast, no contact shredding service.

Call to Action
-- Get a Quote

RECORDS MANAGEMENT
Short Headline:
-- Off-site Records Storage
-- Records Management & Storage
-- Secure Records Storage
-- Records Management Services
-- Long Term Records Management
-- Document Storage Solutions

Possible Description
-- Local, Affordable Storage Solutions. Protect and Store your Documents in our Secure Facility
-- Local, Affordable Records Management Solutions. Store your Records in our Secure Facility
-- Certified, Affordable Document Storage Since 2004. Contact Us for a Free Quote!
-- Vaultmark+ Certified, Affordable Document Storage Since 2004. Contact Us for a Free Quote!

Call to Action
-- Get a Quote

SCANNING SERVICES

Short Headline:
-- Professional Scanning Company
-- Toronto & GTA Scanning Service
-- Document Scanning Services
-- Digital Conversion Services
-- Fast & Easy Retrieval

Description
-- Scan and documents and files with Professional scanning services from Gold-Kettle
-- Convert Your Paper Files to Electronic Files. Fast & Easy Retrieval.
-- Easily access your documents electronically with Document Scanning Services

Call to Action
-- Get a Quote

ALL SERVICES AD SET
Short Headline
-- Shred, Scan & Store Documents
-- Secure Shredding, Records Management and Scanning Services
-- #1 Document Management Company
-- Gold Kettle Shredding, Storage & Scanning

Description
-- Secure and Affordable Toronto & GTA On-Site Shredding, Document Storage & Scanning Company

Call to Action
-- Get a Quote

Font styles to use
Sans Serif

```html
<!DOCTYPE html>
<html lang="en">
<head>
<meta charset="utf-8">
<title>Vantor Reach Ads – Shredding Services Set</title>
<link rel="stylesheet" href="https://fonts.googleapis.com/css2?family=Montserrat:wght@400;500;700;800&family=Poppins:wght@400&display=swap">
<style>
  :root {
    --board-bg: #d6d6d6;
    --label-grey: #9a9a9a;
    --title-grey: #b3b3b3;
    --body-grey: #9c9c9c;
    --ink: #231f20;
    --brand-blue: #1a9ad6;
    --white: #ffffff;
    --band-dark: #262324;
    --photo-deep: #2b9ad8;
    --photo-light: #6cc6ef;
  }
  * { box-sizing: border-box; margin: 0; padding: 0; }
  html, body { width: 1038px; height: 1200px; overflow: hidden; }
  body {
    position: relative;
    background: var(--board-bg);
    font-family: "Montserrat", Arial, sans-serif;
    color: var(--ink);
  }
  .size-label {
    position: absolute;
    font-family: "Poppins", Arial, sans-serif;
    font-size: 17px;
    letter-spacing: 0.5px;
    color: var(--label-grey);
  }
  .ad {
    position: absolute;
    background: var(--white);
    overflow: hidden;
    box-shadow: 6px 8px 8px rgba(0, 0, 0, 0.35);
  }
  .ad-shapes { position: absolute; inset: 0; width: 100%; height: 100%; }
  .photo-fill { fill: url(#photoGradient); stroke: var(--white); stroke-width: 2; }
  .band-fill { fill: var(--band-dark); }
  .headline {
    position: absolute;
    font-weight: 800;
    text-transform: uppercase;
    color: var(--ink);
  }
  .headline .accent { color: var(--brand-blue); }
  .headline span { display: block; }
  .description {
    position: absolute;
    font-weight: 500;
    color: var(--ink);
  }
  .brand-name {
    position: absolute;
    font-weight: 500;
    color: var(--ink);
    line-height: 1;
    white-space: nowrap;
  }
  .cta {
    position: absolute;
    width: 88px;
    height: 28px;
    border-radius: 14px;
    background: var(--white);
    color: #111;
    font-size: 8px;
    font-weight: 800;
    text-transform: uppercase;
    display: flex;
    align-items: center;
    justify-content: center;
    letter-spacing: 0.2px;
  }

  /* Banner 540 x 69 */
  .ad-banner { left: 111px; top: 106px; width: 540px; height: 69px; }
  .ad-banner .brand-name { left: 17px; top: 28px; font-size: 12px; }
  .ad-banner .headline { left: 119px; top: 12px; font-size: 12px; line-height: 12px; }
  .ad-banner .description { left: 221px; top: 16px; font-size: 8px; line-height: 10.5px; }
  .ad-banner .cta { left: 432px; top: 20px; }

  /* Leaderboard 840 x 104 */
  .ad-leaderboard { left: 111px; top: 248px; width: 840px; height: 104px; }
  .ad-leaderboard .brand-name { left: 42px; top: 45px; font-size: 15px; }
  .ad-leaderboard .headline { left: 199px; top: 24px; font-size: 18px; line-height: 19px; }
  .ad-leaderboard .description { left: 373px; top: 31px; font-size: 12px; line-height: 15.5px; }
  .ad-leaderboard .cta { left: 712px; top: 37px; }

  /* Skyscraper 139 x 693 */
  .ad-skyscraper { left: 111px; top: 426px; width: 139px; height: 693px; }
  .ad-skyscraper .headline { left: 17px; top: 53px; font-size: 15.5px; line-height: 16px; }
  .ad-skyscraper .description { left: 20px; top: 142px; font-size: 11.5px; line-height: 15.5px; }
  .ad-skyscraper .brand-name { left: 20px; top: 254px; font-size: 14px; }
  .ad-skyscraper .cta { left: 25px; top: 618px; }

  /* Square 289 x 289 */
  .ad-square { left: 341px; top: 426px; width: 289px; height: 289px; }
  .ad-square .headline { left: 23px; top: 46px; font-size: 17.5px; line-height: 19px; }
  .ad-square .description { left: 25px; top: 126px; font-size: 11.5px; line-height: 15.5px; }
  .ad-square .brand-name { left: 28px; top: 205px; font-size: 13px; }
  .ad-square .cta { left: 176px; top: 227px; }

  .set-title {
    position: absolute;
    left: 341px;
    top: 910px;
    font-size: 50px;
    font-weight: 800;
    letter-spacing: 0.5px;
    color: var(--title-grey);
    text-transform: uppercase;
    white-space: nowrap;
  }
  .set-intro {
    position: absolute;
    left: 344px;
    top: 985px;
    width: 520px;
    font-size: 15px;
    line-height: 26px;
    color: var(--body-grey);
  }
</style>
</head>
<body>

<svg width="0" height="0" style="position:absolute">
  <defs>
    <linearGradient id="photoGradient" x1="0" y1="0" x2="1" y2="1">
      <stop offset="0" stop-color="#4fb5e8"/>
      <stop offset="0.5" stop-color="#2b9ad8"/>
      <stop offset="1" stop-color="#6cc6ef"/>
    </linearGradient>
  </defs>
</svg>

<!-- Banner -->
<div class="size-label" style="left:110px; top:76px;">Banner</div>
<div class="ad ad-banner">
  <svg class="ad-shapes" viewBox="0 0 540 69" preserveAspectRatio="none">
    <path class="band-fill" d="M324,0 H340 L358,34.5 L340,69 H322 L342,34.5 Z"/>
    <path class="photo-fill" role="img" aria-label="Blue-toned photo of hands flipping through stacked paper files" d="M343,0 H541 V70 H343 L361,34.5 Z"/>
  </svg>
  <div class="brand-name">Gold Kettle</div>
  <div class="headline"><span>Secure</span><span class="accent">Shredding</span><span>Services</span></div>
  <div class="description">Certified, Affordable<br>Office Shredding<br>Since 2003.</div>
  <div class="cta">Get a Quote</div>
</div>

<!-- Leaderboard -->
<div class="size-label" style="left:110px; top:219px;">Leaderboard</div>
<div class="ad ad-leaderboard">
  <svg class="ad-shapes" viewBox="0 0 840 104" preserveAspectRatio="none">
    <path class="band-fill" d="M536,0 H552 L574,52 L552,104 H530 L556,52 Z"/>
    <path class="photo-fill" role="img" aria-label="Blue-toned photo of hands flipping through stacked paper files" d="M555,0 H841 V105 H555 L577,52 Z"/>
  </svg>
  <div class="brand-name">Gold Kettle</div>
  <div class="headline"><span>Secure</span><span class="accent">Shredding</span><span>Services</span></div>
  <div class="description">Certified, Affordable<br>Office Shredding<br>Since 2003.</div>
  <div class="cta">Get a Quote</div>
</div>

<!-- Skyscraper -->
<div class="size-label" style="left:110px; top:397px;">Skyscraper</div>
<div class="ad ad-skyscraper">
  <svg class="ad-shapes" viewBox="0 0 139 693" preserveAspectRatio="none">
    <path class="band-fill" d="M0,326 L80,360 L139,332 V354 L80,384 L0,350 Z"/>
    <path class="photo-fill" role="img" aria-label="Blue-toned photo of hands flipping through stacked paper files" d="M-1,352 L80,386 L140,356 V694 H-1 Z"/>
  </svg>
  <div class="headline"><span>Secure</span><span class="accent">Shredding</span><span>Services</span></div>
  <div class="description">Certified,<br>Affordable Office<br>Shredding Since<br>2003.</div>
  <div class="brand-name">Gold Kettle</div>
  <div class="cta">Get a Quote</div>
</div>

<!-- Square -->
<div class="size-label" style="left:336px; top:397px;">Square</div>
<div class="ad ad-square">
  <svg class="ad-shapes" viewBox="0 0 289 289" preserveAspectRatio="none">
    <path class="band-fill" d="M147,0 H160 L200,103 L132,289 H116 L187,103 Z"/>
    <path class="photo-fill" role="img" aria-label="Blue-toned photo of hands flipping through stacked paper files" d="M162,-1 H290 V290 H134 L203,103 Z"/>
  </svg>
  <div class="headline"><span>Secure</span><span class="accent">Shredding</span><span>Services</span></div>
  <div class="description">Certified, Affordable<br>Office Shredding<br>Since 2003.</div>
  <div class="brand-name">Gold Kettle</div>
  <div class="cta">Get a Quote</div>
</div>

<h1 class="set-title">Shredding Services</h1>
<p class="set-intro">Lorem Ipsum is simply dummy text of the printing and typesetting industry. Lorem Ipsum has been.</p>

</body>
</html>
```